We need a fresh, new church business card!!

We need a church business card with basic info to hand out as invites. We are looking for something clean that communicates our basic information clearly.

We are open to square or rectangle card sizes.

The attached logo is the only one that I have available. We'd like to see options with with text of the logo lighter and on a dark background as well as options with white/light backgrounds.

Also, we'd like to see option with rounded corners.

• Address - 2738 Larkmoor Ave., Rockford, IL 61109
• Website - brookvale.church
• Phone - 815-392-6157
• Service times -
• Sunday - 10am Sunday School
• - 11am Family Worship
• - 6pm Night of Prayer
• Wednesday - 7:30pm Adult Bible Study
• Classes for all ages

```html
<!DOCTYPE html>
<html lang="en">
<head>
<meta charset="utf-8">
<title>Brookvale Pentecostal Church – Business Card</title>
<link rel="stylesheet" href="https://fonts.googleapis.com/css2?family=Maven+Pro:wght@400;500;700&display=swap">
<style>
  :root {
    --backdrop: #d9d4ce;
    --card-dark: #221e1c;
    --card-light: #ffffff;
    --accent: #4a8a9a;
    --ink: #5a5a5a;
    --ink-soft: #8c8c8c;
    --white: #ffffff;
    --rule: #d6d6d6;
  }
  * { margin: 0; padding: 0; box-sizing: border-box; }
  html, body {
    width: 1200px; height: 1000px; overflow: hidden;
    background: var(--backdrop);
    font-family: "Maven Pro", sans-serif;
  }
  .canvas { position: relative; width: 1200px; height: 1000px; }

  .card {
    position: absolute; left: 243px; width: 708px; height: 404px;
    box-shadow: 0 8px 24px rgba(0,0,0,.25);
  }
  .card--front { top: 84px; background: var(--card-dark); }
  .card--back { top: 526px; background: var(--card-light); }

  /* Front */
  .front-brand {
    position: absolute; left: 0; right: 0; top: 240px;
    display: flex; justify-content: center; align-items: center; gap: 16px;
    color: var(--white); font-weight: 500;
  }
  .brand-dot { width: 56px; height: 56px; border-radius: 50%; background: var(--accent); flex: none; }
  .brand-name { line-height: 1; }
  .brand-name .primary { display: block; font-size: 44px; letter-spacing: 1px; }
  .brand-name .secondary { display: block; font-size: 14px; letter-spacing: 3.6px; margin-top: 6px; }
  .front-web {
    position: absolute; left: 0; right: 0; top: 336px; text-align: center;
    color: var(--white); font-size: 17px; letter-spacing: .5px;
  }
  .front-web .hl { color: var(--accent); }

  /* Back */
  .back-brand {
    position: absolute; left: 96px; top: 94px;
    display: flex; align-items: center; gap: 10px;
    color: var(--ink); font-weight: 500;
  }
  .back-brand .brand-dot { width: 38px; height: 38px; }
  .back-brand .primary { font-size: 28px; letter-spacing: .5px; }
  .back-brand .secondary { font-size: 9px; letter-spacing: 2.2px; margin-top: 4px; }

  .contact-list {
    position: absolute; left: 96px; top: 164px; list-style: none;
    color: var(--ink); font-size: 17.5px; line-height: 25px;
  }
  .contact-list li { display: flex; align-items: flex-start; gap: 8px; }
  .contact-list li + li { margin-top: 0; }
  .contact-list .gap { margin-top: 6px; }
  .contact-list svg { flex: none; width: 14px; height: 14px; margin-top: 6px; fill: var(--accent); }

  .divider {
    position: absolute; left: 354px; top: 104px; width: 1px; height: 200px;
    background: var(--rule);
  }

  .service-times { position: absolute; left: 389px; top: 98px; color: var(--ink); }
  .service-times h2 {
    color: var(--accent); font-size: 20px; font-weight: 700; letter-spacing: .5px;
    padding-bottom: 4px; border-bottom: 1px solid var(--ink-soft); width: 124px;
    white-space: nowrap;
  }
  .service-times h3 { font-size: 18px; font-weight: 500; margin-top: 6px; line-height: 22px; }
  .service-times h3.later { margin-top: 5px; }
  .service-times ul { list-style: none; font-size: 17.5px; line-height: 25px; }
  .service-times .indent { padding-left: 98px; }
</style>
</head>
<body>
<div class="canvas">

  <section class="card card--front">
    <div class="front-brand">
      <span class="brand-dot"></span>
      <span class="brand-name">
        <span class="primary">BROOKVALE</span>
        <span class="secondary">PENTECOSTAL CHURCH</span>
      </span>
    </div>
    <p class="front-web">www.<span class="hl">brookvale</span>.church</p>
  </section>

  <section class="card card--back">
    <div class="back-brand">
      <span class="brand-dot"></span>
      <span class="brand-name">
        <span class="primary">BROOKVALE</span>
        <span class="secondary">PENTECOSTAL CHURCH</span>
      </span>
    </div>

    <ul class="contact-list">
      <li>
        <svg viewBox="0 0 14 14" aria-hidden="true"><path d="M7 0a5 5 0 0 0-5 5c0 3.6 5 9 5 9s5-5.4 5-9a5 5 0 0 0-5-5zm0 7a2 2 0 1 1 0-4 2 2 0 0 1 0 4z"/></svg>
        <span>2738 Larkmoor Ave.,<br>Rockford, IL 61109</span>
      </li>
      <li class="gap">
        <svg viewBox="0 0 14 14" aria-hidden="true"><path d="M1 5c0-2 2.5-3 6-3s6 1 6 3v1h-3V4.5H4V6H1zM3 7h8l1.5 5h-11z"/></svg>
        <span>(815) 392-6157</span>
      </li>
      <li>
        <svg viewBox="0 0 14 14" aria-hidden="true"><path d="M7 1a6 6 0 1 0 0 12A6 6 0 0 0 7 1zm0 1.2c.6.7 1.1 1.7 1.3 2.8H5.7C5.9 3.9 6.4 2.9 7 2.2zM2.3 8a4.8 4.8 0 0 1 0-2h2.2a9 9 0 0 0 0 2zm3.4 1h2.6C8.1 10.1 7.6 11.1 7 11.8 6.4 11.1 5.9 10.1 5.7 9zm2.8-1H5.5a8 8 0 0 1 0-2h3a8 8 0 0 1 0 2zm1 0a9 9 0 0 0 0-2h2.2a4.8 4.8 0 0 1 0 2z"/></svg>
        <span>www.brookvale.church</span>
      </li>
      <li>
        <svg viewBox="0 0 14 14" aria-hidden="true"><circle cx="7" cy="7" r="5"/></svg>
        <span>brookvale.church</span>
      </li>
      <li>
        <svg viewBox="0 0 14 14" aria-hidden="true"><circle cx="7" cy="7" r="5"/></svg>
        <span>_brookvale</span>
      </li>
    </ul>

    <div class="divider"></div>

    <div class="service-times">
      <h2>Service Times</h2>
      <h3>Sunday</h3>
      <ul>
        <li>- 10am Sunday School</li>
        <li>- 11am Worship Service</li>
        <li>- 6pm Night of Prayer</li>
      </ul>
      <h3 class="later">Wednesday</h3>
      <ul>
        <li>- 7:30pm Adult Bible Study</li>
        <li class="indent">- Kids' Classes</li>
      </ul>
    </div>
  </section>

</div>
</body>
</html>
```